Clinical Hypnotherapy

I need a flyer to promote my services as a highly qualified Clinical Hypnotherapist . This flyer will be distributed at various alternative health clinic where I see clients and should explain to the client what hypnotherapy is and how it can help them . I would like it to match my website ( www.brenwickcalm.co.uk ) as closely as possible in terms of the images , fonts and colours used . For this reason I include the following information that was supplied by the web designers :
Image : www.pixavane.com - photo no. 4817265
Fonts in banner : Avenir Next Condensed , Arial Narrow
Main colour used for background : #0b3166
Attached is a file with text . Depending on available space I can provide additional text or if neccesary remove text .
Kindly also inform me of the cost prior to going ahead
Updates
Thank you for designs submitted so far . My fault but I realise that I originally included way too much text in my brief . Please find new attachment with reduced text . This will hopefully allow for a more eye catching less cluttered design . I would also like to have a logo designed for Brenwick Calm - something abstract which reflects the psychotherapeutic / mind nature of the therapy .
Industry/Entity Type
Hypnotherapy
Look and feel
Each slider illustrates characteristics of the customer's brand and the style your logo design should communicate.

```html
<!DOCTYPE html>
<html lang="en">
<head>
<meta charset="utf-8">
<title>Brenwick Calm – Clinical Hypnotherapy Flyer</title>
<link href="https://fonts.googleapis.com/css2?family=PT+Sans:wght@400;700&family=Roboto+Condensed:wght@700&display=swap" rel="stylesheet">
<style>
  :root {
    --navy: #0b3166;
    --navy-deep: #082650;
    --blue: #1d5fa8;
    --blue-bright: #2f7fd0;
    --sky-light: #cfe6f7;
    --sky-mid: #7fb6e0;
    --link-blue: #2a6fb8;
    --text-dark: #2b2b2b;
    --tab-grey: #e6e8eb;
    --tab-text: #4a4f55;
    --white: #ffffff;
  }
  * { margin: 0; padding: 0; box-sizing: border-box; }
  html, body { width: 848px; height: 1200px; overflow: hidden; background: var(--white); }
  .flyer {
    position: relative;
    width: 848px;
    height: 1200px;
    overflow: hidden;
    background: var(--white);
    font-family: "PT Sans", Arial, sans-serif;
    color: var(--text-dark);
  }
  .hero-photo {
    position: absolute;
    left: 0; top: 0;
    width: 848px; height: 420px;
    background:
      radial-gradient(ellipse at 55% 35%, rgba(255,255,255,0.95) 0%, rgba(255,255,255,0) 28%),
      linear-gradient(180deg, var(--sky-light) 0%, var(--sky-mid) 45%, #3f86c8 75%, var(--blue) 100%);
  }
  .hero-wave { position: absolute; left: 0; top: 240px; width: 848px; height: 220px; }
  .section-tab {
    position: absolute;
    left: 30px;
    height: 34px;
    padding: 0 28px 0 12px;
    border-radius: 4px 18px 18px 4px;
    background: var(--tab-grey);
    box-shadow: 2px 3px 5px rgba(0,0,0,0.3);
    font-family: "Roboto Condensed", "Arial Narrow", sans-serif;
    font-weight: 700;
    font-size: 27px;
    line-height: 34px;
    text-transform: uppercase;
    letter-spacing: 0.3px;
  }
  .section-tab .accent { color: var(--link-blue); }
  .section-tab .plain { color: var(--tab-text); }
  .about-tab { top: 473px; }
  .about-text {
    position: absolute;
    left: 40px; top: 522px;
    width: 775px;
    font-size: 17.4px;
    line-height: 23px;
  }
  .about-text p + p { margin-top: 23px; }
  .hypnosis-band {
    position: absolute;
    left: 0; top: 808px;
    width: 848px; height: 228px;
    background: linear-gradient(180deg, #5e8fc8 0%, #1f559a 14%, var(--navy) 45%, var(--navy-deep) 100%);
    box-shadow: 0 6px 10px rgba(0,0,0,0.25);
  }
  .hypnosis-tab { top: 843px; }
  .hypnosis-text {
    position: absolute;
    left: 40px; top: 894px;
    width: 775px;
    font-size: 17.4px;
    line-height: 23px;
    color: #e8eef7;
  }
  .contact {
    position: absolute;
    left: 40px; top: 1066px;
    width: 640px;
    font-size: 17.4px;
    line-height: 22px;
  }
  .contact .highlight { color: var(--link-blue); font-weight: 700; }
  .member-badge { position: absolute; left: 695px; top: 1056px; width: 110px; height: 110px; }
</style>
</head>
<body>
<div class="flyer">
  <div class="hero-photo" role="img" aria-label="Calm sea and sky photo with a grid of translucent tiles showing smiling client portraits"></div>
  <svg class="hero-wave" viewBox="0 0 848 220" aria-hidden="true">
    <defs>
      <linearGradient id="waveBlue" x1="0" y1="0" x2="1" y2="0">
        <stop offset="0" stop-color="#0d3a7a"/>
        <stop offset="0.6" stop-color="#1d5fa8"/>
        <stop offset="1" stop-color="#2f7fd0"/>
      </linearGradient>
      <linearGradient id="waveShade" x1="0" y1="0" x2="0" y2="1">
        <stop offset="0" stop-color="#c7ccd3"/>
        <stop offset="1" stop-color="#ffffff"/>
      </linearGradient>
    </defs>
    <path d="M0 90 Q 360 150 848 40 L848 220 L0 220 Z" fill="url(#waveBlue)"/>
    <path d="M0 125 Q 380 170 848 80 L848 220 L0 220 Z" fill="#123f80" opacity="0.6"/>
    <path d="M0 140 Q 420 175 848 105 L848 220 L0 220 Z" fill="url(#waveShade)"/>
    <path d="M0 175 Q 440 185 848 130 L848 220 L0 220 Z" fill="#ffffff"/>
  </svg>

  <div class="section-tab about-tab"><span class="accent">About</span> <span class="plain">Me</span></div>
  <div class="about-text">
    <p>I am a certified and accredited Hypnotherapist with a Post Graduate Certificate and Diploma in Clinical Hypnotherapy from the Halvern College of Clinical Hypnosis (HCCH) . I see clients at my clinic in Brenwick , The Stillwater Therapy Centre in Forest Hill and The Orrin Clinic in Marylebone.</p>
    <p>I work with a wide range of conditions but have come to specialise in weight loss and eating disorders as well as anxiety and stress-related conditions. I make use of an eclectic range of techniques, including Clinical Hypnosis, Cognitive Behavioural Hypnosis (CBH), Mindfulness , Eye Movement Desensitization and Reprocessing (EMDR) and Ego State Therapy, in order to tailor therapy to your unique needs and to help achieve a positive outcome.</p>
  </div>

  <div class="hypnosis-band"></div>
  <div class="section-tab hypnosis-tab"><span class="accent">Hypnosis</span></div>
  <div class="hypnosis-text">
    <p>Hypnotherapy is neither mystical nor magical but it can help effect extraordinary, and often rapid change in peoples’ lives, by helping to change subconscious beliefs, habits and associations. Hypnotherapy is a solution-focussed approach which provides you with the tools and resources to take control of your life, improve your self-esteem and develop self-confidence.</p>
  </div>

  <div class="contact">
    <p>Why not call me on <span class="highlight">075 0612 4437</span> or<br>
    email me at <span class="highlight">daniel@brenwickcalm.co.uk</span> for a quick, friendly,<br>
    no-obligation consultation.<br>
    More information can be found at <span class="highlight">www.brenwickcalm.co.uk</span></p>
  </div>

  <svg class="member-badge" viewBox="0 0 110 110" role="img" aria-label="Professional membership badge">
    <circle cx="55" cy="55" r="52" fill="#1a1a1a"/>
    <circle cx="55" cy="55" r="34" fill="#ffffff"/>
  </svg>
</div>
</body>
</html>
```